4 x Designs Required

Hi There,
I require 4 x different designs to be made for 4 new brands of mine however they can be quite interchangeable. HR Plinkr and Marketing Plinkr can be similar just with a difference in colour. The same goes for the Bulletin brands. This means there are ultimately two designs that need perfecting.

There must be a click here CTA on the banner somewhere. :-)

I require the banners in 728x90 format and 960x90 please.

Please use strap lines on the banners such as:
Essential Whitepapers for HR Professionals
Essential Whitepapers for Marketing Professionals
Your No.1 Whitepaper Resource

The brand names:
HR Plinkr
Marketing Plinkr
HR Dispatchly
Marketing Dispatchly

Examples attached.

```html
<!DOCTYPE html>
<html lang="en">
<head>
<meta charset="utf-8">
<title>Plinkr Banner Set</title>
<link rel="stylesheet" href="https://fonts.googleapis.com/css2?family=Montserrat:wght@600;700;800&family=Mulish:wght@500;600;700&display=swap">
<style>
  :root {
    --page: #ffffff;
    --mkt-navy: #0a1822;
    --mkt-deep: #071219;
    --mkt-teal: #1fe3c0;
    --mkt-glow: #0e6f63;
    --mkt-ink: #0b2a2b;
    --hr-green: #0f5a45;
    --hr-dark: #0b4a38;
    --hr-lime: #7fe06b;
    --hr-dots: #a8d94f;
    --hr-ink: #0d3d2c;
    --white: #ffffff;
  }
  * { box-sizing: border-box; margin: 0; padding: 0; }
  html, body { width: 1200px; height: 763px; overflow: hidden; background: var(--page); }
  .canvas { position: relative; width: 1200px; height: 763px; }

  .banner { position: absolute; overflow: hidden; }
  .banner__pattern { position: absolute; }
  .brand, .strapline, .cta { position: absolute; }
  .strapline { font-family: "Mulish", sans-serif; font-weight: 500; color: var(--white); white-space: nowrap; }

  /* Marketing banners */
  .banner--marketing { background: var(--mkt-navy); }
  .brand--marketing { font-family: "Montserrat", sans-serif; font-weight: 800; color: var(--mkt-teal); line-height: 0.95; text-transform: uppercase; }
  .brand--marketing .brand__top { display: block; }
  .brand--marketing .brand__main { display: block; }
  .accent--teal { color: var(--mkt-teal); }
  .cta-circle { position: absolute; overflow: visible; }
  .cta-circle text { font-family: "Montserrat", sans-serif; font-weight: 700; fill: var(--mkt-ink); }

  .banner--mkt-large { left: 64px; top: 60px; width: 1073px; height: 131px; }
  .banner--mkt-large .banner__pattern { left: 360px; top: 0; width: 713px; height: 131px;
    background: radial-gradient(ellipse 420px 160px at 470px 110px, var(--mkt-glow) 0%, rgba(14,111,99,0.35) 45%, rgba(10,24,34,0) 80%); }
  .banner--mkt-large .brand { left: 38px; top: 40px; }
  .banner--mkt-large .brand__top { font-size: 15px; color: var(--white); }
  .banner--mkt-large .brand__main { font-size: 15px; }
  .banner--mkt-large .strapline { left: 221px; top: 49px; font-size: 27px; }

  .banner--mkt-small { left: 68px; top: 243px; width: 1066px; height: 66px; background: var(--mkt-deep); }
  .banner--mkt-small .banner__pattern { left: 620px; top: 0; width: 446px; height: 66px;
    background: radial-gradient(ellipse 260px 90px at 370px 34px, rgba(31,227,192,0.35) 0%, rgba(14,111,99,0.2) 50%, rgba(7,18,25,0) 85%); }
  .banner--mkt-small .brand { left: 49px; top: 16px; }
  .banner--mkt-small .brand__top { font-size: 11px; }
  .banner--mkt-small .brand__main { font-size: 11px; }
  .banner--mkt-small .strapline { left: 252px; top: 19px; font-size: 24px; }

  /* HR banners */
  .banner--hr { background: var(--hr-green); }
  .brand--hr { font-family: "Montserrat", sans-serif; font-weight: 800; color: var(--white); white-space: nowrap; }
  .strapline__strong { font-weight: 700; }
  .cta--pill { display: flex; align-items: center; justify-content: center; background: var(--hr-lime);
    border-radius: 999px; font-family: "Montserrat", sans-serif; font-weight: 600; color: var(--hr-ink); }
  .pattern--left { background: radial-gradient(ellipse at 0% 100%, rgba(127,224,107,0.35) 0%, rgba(15,90,69,0) 70%); }
  .pattern--right { background: radial-gradient(ellipse at 85% 60%, rgba(168,217,79,0.55) 0%, rgba(127,224,107,0.2) 45%, rgba(15,90,69,0) 75%); }

  .banner--hr-large { left: 53px; top: 418px; width: 1093px; height: 134px; }
  .banner--hr-large .pattern--left { left: 0; top: 40px; width: 160px; height: 94px; }
  .banner--hr-large .pattern--right { left: 760px; top: 0; width: 333px; height: 134px; }
  .banner--hr-large .brand { left: 41px; top: 40px; font-size: 42px; }
  .banner--hr-large .strapline { left: 291px; top: 51px; font-size: 26px; }
  .banner--hr-large .cta { left: 894px; top: 42px; width: 159px; height: 46px; font-size: 21px; }

  .banner--hr-small { left: 58px; top: 600px; width: 1083px; height: 67px; }
  .banner--hr-small .pattern--left { left: 0; top: 0; width: 140px; height: 67px; }
  .banner--hr-small .pattern--right { left: 780px; top: 0; width: 303px; height: 67px; }
  .banner--hr-small .brand { left: 62px; top: 10px; font-size: 38px; }
  .banner--hr-small .strapline { left: 304px; top: 19px; font-size: 24px; }
  .banner--hr-small .cta { left: 882px; top: 13px; width: 131px; height: 39px; font-size: 18px; }
</style>
</head>
<body>
<main class="canvas">

  <section class="banner banner--marketing banner--mkt-large" aria-label="Marketing Plinkr 960x90 banner">
    <div class="banner__pattern" role="img" aria-label="Concentric ripple pattern glowing in teal"></div>
    <div class="brand brand--marketing"><span class="brand__top">Marketing</span><span class="brand__main">Plinkr</span></div>
    <p class="strapline">Essential Whitepapers for <span class="accent--teal">Marketing Professionals</span></p>
    <svg class="cta-circle" style="left:876px;top:-25px" width="200" height="190" viewBox="0 0 200 190" aria-label="Click here">
      <circle cx="96" cy="96" r="95" fill="none" stroke="#1fe3c0" stroke-width="1.5"/>
      <circle cx="96" cy="96" r="84" fill="#1fe3c0"/>
      <text x="96" y="103" font-size="19" text-anchor="middle">CLICK HERE</text>
    </svg>
  </section>

  <section class="banner banner--marketing banner--mkt-small" aria-label="Marketing Plinkr 728x90 banner">
    <div class="banner__pattern" role="img" aria-label="Concentric ripple pattern in teal"></div>
    <div class="brand brand--marketing"><span class="brand__top">Marketing</span><span class="brand__main">Plinkr</span></div>
    <p class="strapline">Essential Whitepapers for <span class="accent--teal">Marketing Professionals</span></p>
    <svg class="cta-circle" style="left:930px;top:-22px" width="120" height="110" viewBox="0 0 120 110" aria-label="Click here">
      <circle cx="58" cy="56" r="57" fill="none" stroke="#1fe3c0" stroke-width="1.2"/>
      <circle cx="58" cy="56" r="50" fill="#1fe3c0"/>
      <text x="58" y="61" font-size="12.5" text-anchor="middle">CLICK HERE</text>
    </svg>
  </section>

  <section class="banner banner--hr banner--hr-large" aria-label="HR Plinkr 960x90 banner">
    <div class="banner__pattern pattern--left" role="img" aria-label="Halftone dot texture in green"></div>
    <div class="banner__pattern pattern--right" role="img" aria-label="Halftone dot wave in lime and yellow"></div>
    <div class="brand brand--hr">HR Plinkr</div>
    <p class="strapline">Essential Whitepapers <span class="strapline__strong">for HR Professionals</span></p>
    <a class="cta cta--pill">Click Here</a>
  </section>

  <section class="banner banner--hr banner--hr-small" aria-label="HR Plinkr 728x90 banner">
    <div class="banner__pattern pattern--left" role="img" aria-label="Halftone dot texture in green"></div>
    <div class="banner__pattern pattern--right" role="img" aria-label="Halftone dot wave in lime and yellow"></div>
    <div class="brand brand--hr">HR Plinkr</div>
    <p class="strapline">Essential Whitepapers <span class="strapline__strong">for HR Professionals</span></p>
    <a class="cta cta--pill">Click Here</a>
  </section>

</main>
</body>
</html>
```